Healthcare and Professional IT Services Company need a redesigned business card

We are a IT Services company that targets small medical practices and professional business such as Attorneys, Accounts, Architects etc. We want to communicate a professional yet friendly image using recent logo redesign here on Sketchforge. Like to see the colors blue and orange in the design. Must use the Copper Lantern Technology as displayed in the new logo - then also want to incorporate the fish logo as well.

Target Market(s)

Small medical and professional services

Industry/Entity Type

It Company

Contact Information for Business Card

The usual stuff, place for name address phone website. Also maybe our tagline which is "Guiding your technology"

Requirements
Must have
• My new logo and the fish somewhere on the card

```html
<!DOCTYPE html>
<html lang="en">
<head>
<meta charset="utf-8">
<title>Copper Lantern Technology – Business Card</title>
<link rel="stylesheet" href="https://fonts.googleapis.com/css2?family=Open+Sans:wght@400;600&family=Ubuntu:wght@500;700&display=swap">
<style>
  :root {
    --backdrop: #dcdcdc;
    --brand-blue: #0f9ddc;
    --deep-blue: #1a74b8;
    --accent-orange: #f7941d;
    --paper: #ffffff;
    --ink: #555a5e;
  }
  * { margin: 0; padding: 0; box-sizing: border-box; }
  html, body {
    width: 1200px;
    height: 900px;
    overflow: hidden;
    background: var(--backdrop);
  }
  .canvas {
    position: relative;
    width: 1200px;
    height: 900px;
  }
  .card {
    position: absolute;
    left: 300px;
    width: 600px;
    height: 343px;
    box-shadow: 0 6px 18px rgba(0,0,0,0.18);
  }
  .card-back {
    top: 60px;
    background: var(--brand-blue);
  }
  .back-mark {
    position: absolute;
    left: 50%;
    top: 120px;
    transform: translateX(-50%);
    font-family: "Ubuntu", sans-serif;
    font-weight: 500;
    font-size: 34px;
    color: var(--paper);
    white-space: nowrap;
  }
  .tagline {
    position: absolute;
    left: 130px;
    bottom: 34px;
    font-family: "Open Sans", sans-serif;
    font-size: 15px;
    color: var(--paper);
  }
  .card-front {
    top: 497px;
    background: var(--paper);
  }
  .front-logo {
    position: absolute;
    left: 40px;
    top: 40px;
    display: flex;
    align-items: center;
    gap: 10px;
    font-family: "Ubuntu", sans-serif;
    font-weight: 500;
    font-size: 28px;
    color: var(--brand-blue);
    white-space: nowrap;
  }
  .front-logo .logo-dot {
    width: 16px;
    height: 16px;
    border-radius: 50%;
    background: var(--brand-blue);
  }
  .contact-list {
    position: absolute;
    left: 40px;
    top: 118px;
    list-style: none;
    font-family: "Open Sans", sans-serif;
    font-size: 14px;
    color: var(--ink);
  }
  .contact-list li {
    display: flex;
    align-items: center;
    gap: 10px;
    height: 24px;
  }
  .contact-list svg { width: 14px; height: 14px; flex: none; }
  .person {
    position: absolute;
    right: 40px;
    top: 120px;
    text-align: right;
  }
  .person-name {
    font-family: "Ubuntu", sans-serif;
    font-weight: 700;
    font-size: 24px;
    color: var(--brand-blue);
  }
  .person-role {
    font-family: "Open Sans", sans-serif;
    font-size: 17px;
    color: var(--accent-orange);
  }
  .address {
    position: absolute;
    right: 40px;
    bottom: 34px;
    text-align: right;
    font-family: "Open Sans", sans-serif;
    font-style: normal;
    font-size: 15px;
    line-height: 1.5;
    color: var(--ink);
  }
</style>
</head>
<body>
<main class="canvas">
  <section class="card card-back">
    <p class="back-mark">Copper Lantern Technology</p>
    <p class="tagline">Guiding your technology</p>
  </section>

  <section class="card card-front">
    <div class="front-logo"><span class="logo-dot"></span>Copper Lantern Technology</div>

    <ul class="contact-list">
      <li>
        <svg viewBox="0 0 14 14" aria-hidden="true"><path d="M3 1h3l1 3-2 1.2a7 7 0 0 0 3.8 3.8L10 7l3 1v3a2 2 0 0 1-2 2A10 10 0 0 1 1 3a2 2 0 0 1 2-2z" fill="var(--brand-blue)"/></svg>
        555 210 4816
      </li>
      <li>
        <svg viewBox="0 0 14 14" aria-hidden="true"><rect x="0.5" y="2.5" width="13" height="9" rx="1" fill="var(--brand-blue)"/><path d="M1 3.5l6 4.5 6-4.5" fill="none" stroke="#fff" stroke-width="1.2"/></svg>
        hello@copperlantern.example
      </li>
      <li>
        <svg viewBox="0 0 14 14" aria-hidden="true"><circle cx="7" cy="7" r="6.5" fill="var(--brand-blue)"/><ellipse cx="7" cy="7" rx="2.8" ry="6" fill="none" stroke="#fff" stroke-width="1"/><path d="M1 7h12" stroke="#fff" stroke-width="1"/></svg>
        www.copperlantern.example
      </li>
    </ul>

    <div class="person">
      <p class="person-name">Dana Whitlow</p>
      <p class="person-role">CEO/Founder</p>
    </div>

    <address class="address">
      412 Harbor Bend Road<br>
      Juneau, Alaska 99801
    </address>
  </section>
</main>
</body>
</html>
```